Commercial photographer, UAV drone photography & 360 walk-through visuals

I need a business card design that is minimalist but yet pretentiously creative. My target market are architects, designers, advertising agents and marketing managers. It is important to stress that though I am asking for a minimalist design it needs to have creative impact.

Target Market(s)

Architects, interiors designers, web-designers, artists

Contact Information for Business Card

Include my name, mobile [cell] number, email, web page and the company logo. Do not to include a postal address.

Colors

Designer to choose colors to be used in the design.

Requirements
Must have
• The following information is to be included:
• Miles Perrow
• Photographer
• m: 07812 593174
• e: miles@mpframeworks.co.uk
• w: mpframeworks.co.uk

```html
<!DOCTYPE html>
<html lang="en">
<head>
<meta charset="utf-8">
<title>MP Frameworks – Business Card</title>
<link rel="stylesheet" href="https://fonts.googleapis.com/css2?family=Jost:ital,wght@0,300;0,400;0,500;1,400&display=swap">
<style>
  :root{
    --stage:#6b6b6b;
    --ink:#231f20;
    --paper:#ffffff;
    --orange:#ee6a24;
    --rust-line:#5c3b2f;
    --peach-light:#fbdfcb;
    --peach-dusty:#e5cbbd;
    --text-dark:#1e1e1e;
  }
  *{box-sizing:border-box;margin:0;padding:0}
  html,body{width:1200px;height:1200px;overflow:hidden}
  body{background:var(--stage);position:relative;font-family:"Jost",sans-serif}

  .card{position:absolute;left:281px;width:638px;height:389px;overflow:hidden}
  .card--front{top:170px;background:var(--ink)}
  .card--back{top:635px;background:var(--paper)}

  .card-lines{position:absolute;inset:0}

  .brand{position:absolute;color:var(--paper);font-weight:300;text-transform:uppercase;line-height:1}
  .brand--front{left:100px;top:110px;display:flex;align-items:center;gap:22px}
  .brand-dot{width:40px;height:40px;border-radius:50%;background:var(--paper);flex:none}
  .brand-words{display:flex;flex-direction:column;gap:10px}
  .brand-line1{font-size:50px;letter-spacing:6px}
  .brand-line2{font-size:56px;letter-spacing:4px}

  .back-decor{position:absolute;inset:0;
    background:linear-gradient(160deg,var(--peach-light) 0%,var(--peach-light) 45%,var(--peach-dusty) 100%);
    clip-path:polygon(100% 18%,100% 100%,2% 100%,14% 84%,45% 72%,56% 40%,78% 22%)}

  .holder{position:absolute;left:65px;top:40px;text-align:center;width:232px}
  .holder-name{font-size:36px;font-weight:400;color:var(--orange);letter-spacing:.5px;line-height:1.1}
  .holder-role{font-size:24px;font-style:italic;color:var(--text-dark);margin-top:4px}

  .contact-tab{position:absolute;left:0;top:146px;width:73px;height:191px;background:var(--orange);border-radius:0 24px 24px 0}
  .contact-list{position:absolute;left:0;top:146px;list-style:none}
  .contact-item{position:absolute;left:0;height:30px;display:flex;align-items:center;white-space:nowrap}
  .contact-item svg{width:26px;height:26px;margin-left:22px;flex:none}
  .contact-item span{margin-left:47px;font-size:22px;font-weight:400;color:var(--text-dark);letter-spacing:.4px}

  .logo-frame{position:absolute;left:358px;top:134px;width:252px;height:120px}
  .brand--back{left:30px;top:43px;color:var(--text-dark);font-size:24px;font-weight:400;letter-spacing:2px;display:flex;align-items:center;gap:10px}
  .brand--back .brand-dot{width:14px;height:14px;background:var(--text-dark)}
</style>
</head>
<body>

<section class="card card--front">
  <svg class="card-lines" viewBox="0 0 638 389" width="638" height="389" aria-hidden="true">
    <line x1="0" y1="389" x2="613" y2="0" stroke="var(--rust-line)" stroke-width="2"/>
    <line x1="19" y1="389" x2="638" y2="91" stroke="var(--rust-line)" stroke-width="2"/>
    <line x1="92" y1="24" x2="316" y2="24" stroke="var(--orange)" stroke-width="3"/>
    <line x1="597" y1="241" x2="597" y2="389" stroke="var(--orange)" stroke-width="3"/>
    <line x1="386" y1="366" x2="583" y2="366" stroke="var(--orange)" stroke-width="3"/>
  </svg>
  <div class="brand brand--front">
    <span class="brand-dot"></span>
    <div class="brand-words">
      <span class="brand-line1">MP</span>
      <span class="brand-line2">Frameworks</span>
    </div>
  </div>
</section>

<section class="card card--back">
  <div class="back-decor" role="img" aria-label="Soft peach tiled perspective pattern"></div>

  <div class="holder">
    <p class="holder-name">YOUR NAME</p>
    <p class="holder-role">Director</p>
  </div>

  <div class="contact-tab"></div>
  <ul class="contact-list">
    <li class="contact-item" style="top:21px">
      <svg viewBox="0 0 24 24"><path fill="#fff" d="M12 2a7 7 0 0 0-7 7c0 5 7 13 7 13s7-8 7-13a7 7 0 0 0-7-7zm0 9.5A2.5 2.5 0 1 1 12 6.5a2.5 2.5 0 0 1 0 5z"/></svg>
      <span>Lorem ipsum</span>
    </li>
    <li class="contact-item" style="top:64px">
      <svg viewBox="0 0 24 24" fill="none" stroke="#fff" stroke-width="2"><circle cx="12" cy="12" r="9.5"/><ellipse cx="12" cy="12" rx="4" ry="9.5"/><line x1="2.5" y1="12" x2="21.5" y2="12"/><path d="M4.5 7h15M4.5 17h15"/></svg>
      <span>Lorem ipsum</span>
    </li>
    <li class="contact-item" style="top:107px">
      <svg viewBox="0 0 24 24" fill="none" stroke="#fff" stroke-width="2"><rect x="2" y="5" width="20" height="14"/><path d="M2 5l10 8 10-8M2 19l7-7M22 19l-7-7"/></svg>
      <span>Lorem ipsum</span>
    </li>
    <li class="contact-item" style="top:147px">
      <svg viewBox="0 0 24 24"><path fill="#fff" d="M6.6 10.8a15 15 0 0 0 6.6 6.6l2.2-2.2a1 1 0 0 1 1-.25 11.4 11.4 0 0 0 3.6.57 1 1 0 0 1 1 1V20a1 1 0 0 1-1 1A17 17 0 0 1 3 4a1 1 0 0 1 1-1h3.5a1 1 0 0 1 1 1c0 1.25.2 2.45.57 3.57a1 1 0 0 1-.25 1z"/></svg>
      <span>Lorem ipsum</span>
    </li>
  </ul>

  <div class="logo-frame">
    <svg viewBox="0 0 252 120" width="252" height="120" aria-hidden="true" style="position:absolute;inset:0">
      <path d="M10 14V3h238v12M248 30v84H3V60" fill="none" stroke="var(--orange)" stroke-width="6"/>
    </svg>
    <div class="brand brand--back"><span class="brand-dot"></span>MP Frameworks</div>
  </div>
</section>

</body>
</html>
```